Healthcare Information Interoperability Effort Needs a Roadmap Graphic

Interoperability of healthcare information is critical to accelerated research and improved patient outcomes. We are seeking a graphic to illustrate our roadmap for achieving healthcare information interoperability.

The roadmap has four key components. Please refer to this link for more information about direction and guide in the presentation.
https://lnkvyro.example/q7Zp3m

Industry/Entity Type

Healthcare

Font styles to use
Sans Serif

Requirements
Must have
• See https://lnkvyro.example/q7Zp3m
Nice to have

```html
<!DOCTYPE html>
<html lang="en">
<head>
<meta charset="utf-8">
<title>Semantic Interoperability Roadmap</title>
<link rel="stylesheet" href="https://fonts.googleapis.com/css2?family=Arimo:wght@400&display=swap">
<style>
  :root {
    --bg: #5e5e5c;
    --hub-blue: #0a4899;
    --white: #ffffff;
    --centre-text: #dcdcdc;
    --technical: #1aa3e0;
    --policy: #f39200;
    --social: #8dc63f;
  }
  html, body {
    margin: 0;
    padding: 0;
    width: 1200px;
    height: 1000px;
    overflow: hidden;
    background: var(--bg);
  }
  .roadmap {
    position: relative;
    width: 1200px;
    height: 1000px;
    font-family: "Arimo", Arial, sans-serif;
  }
  .roadmap__shape {
    position: absolute;
    inset: 0;
  }
  .hub-fill { fill: var(--hub-blue); }
  .hub-hole { fill: var(--bg); }

  .node-label,
  .action,
  .centre-label {
    position: absolute;
    margin: 0;
    font-weight: 400;
    white-space: nowrap;
  }
  .node-label {
    color: var(--white);
    font-size: 45px;
    line-height: 1;
  }
  .node-label--technical { left: 723px; top: 235px; }
  .node-label--policy { left: 338px; top: 487px; }
  .node-label--social { left: 772px; top: 712px; }

  .centre-label {
    left: 656px;
    top: 443px;
    transform: translateX(-50%);
    text-align: center;
    color: var(--centre-text);
    font-size: 35px;
    line-height: 43px;
  }

  .action {
    font-size: 35px;
    line-height: 43px;
  }
  .action--technical { left: 937px; top: 203px; color: var(--technical); }
  .action--technical span { display: block; padding-left: 9px; }
  .action--policy { left: 20px; top: 462px; color: var(--policy); }
  .action--social { left: 953px; top: 661px; color: var(--social); }
</style>
</head>
<body>
<main class="roadmap">
  <svg class="roadmap__shape" width="1200" height="1000" viewBox="0 0 1200 1000" aria-hidden="true">
    <g class="hub">
      <circle class="hub-fill" cx="790" cy="245" r="135"/>
      <circle class="hub-fill" cx="390" cy="497" r="135"/>
      <circle class="hub-fill" cx="808" cy="718" r="135"/>
      <path class="hub-fill" d="M470,388 C540,385 610,330 658,272 L790,245 L858,362 C825,410 822,545 855,595 L808,718 L685,660 C620,620 530,600 465,610 L390,497 Z"/>
    </g>
    <path class="hub-hole" d="M532,456 C580,400 650,360 732,358 Q752,358 760,376 C792,450 792,530 760,598 Q750,614 732,614 C650,610 580,560 532,486 Q522,471 532,456 Z"/>
  </svg>

  <p class="centre-label">Semantic<br>Interoperability</p>

  <p class="node-label node-label--technical">technical</p>
  <p class="node-label node-label--policy">policy</p>
  <p class="node-label node-label--social">social</p>

  <p class="action action--technical">standardize the<span>standards</span></p>
  <p class="action action--policy">incentivize<br>interoperability</p>
  <p class="action action--social">crowdsource<br>mappings</p>
</main>
</body>
</html>
```